HR Outsourcing and Payroll Company needs a website re-design

The client is VireloStaffHR: www .virelostaff. example

They provide services to other businesses, specifically Human Resources (HR) Outsourcing and Payroll services. They are not happy with their current website and have retained our agency to provide a re-design.

You will design 4 pages for us to show the client. They will select a design they like. My agency will take the winning design and files and design the remaining pages of the site. But, we need you to help us establish a design for the basics so they can select a direction.

We need a Homepage design, a Service Page design, a Broker page design, and a Contact page design.

They really like these websites (in order from most preferred look and feel of imagery and design elements), so I think a mix between the two would be great:

https://www.brandleworks.example/
http://www.quopaly.example/

I have attached a project brief for this website. Please refer to it... It will help you be successful in what you deliver. The best designs will incorporate functionality and elements from the project brief.

Target Market(s)

Business owners. They will be thinking about thinks like employee reviews, payroll, time keeping, hiring, being compliant with state laws, and needing an expert to help them.

Industry/Entity Type

It Company

Number of Pages Required

4 page

Font styles to use
Sans Serif

Colors
f37122
0255a3
fbed22
9bcb3c
ec1f27

Requirements
Must have
• We need:
• -Homepage design (desktop and mobile)
• -Service Page design (desktop and mobile)
• -Broker page design (desktop and mobile)
• -Contact page design (desktop and mobile)
• Inspiration: a mix between the two would be great:
• https://www.brandleworks.example/
• http://www.quopaly.example/
• They like the long extended homepage look:
• http://www.quopaly.example/
• Photos that have focused people in the front and blurred backgrounds. Example: https://www.brandleworks.example/
• Graphic Icons for their services. Example:
• http://www.quopaly.example/
• I have attached a project brief for this website. Please refer to it... It will help you be successful in what you deliver. The best designs will incorporate functionality and elements from the project brief.
Should not have
• Crappy stock photos... you can use watermarked stock photos if you don't wish to purchase them for the sake of the contest.

```html
<!DOCTYPE html>
<html lang="en">
<head>
<meta charset="utf-8">
<title>VireloStaffHR – HR Outsourcing &amp; Payroll</title>
<link href="https://fonts.googleapis.com/css2?family=Roboto:wght@300;400;500;700&display=swap" rel="stylesheet">
<style>
:root{
  --blue:#0255a3;
  --blue-dark:#013f7a;
  --orange:#f37122;
  --yellow:#fbed22;
  --green:#9bcb3c;
  --red:#ec1f27;
  --ink:#333;
  --muted:#888;
  --line:#e2e2e2;
  --soft:#f3f3f3;
}
*{box-sizing:border-box;margin:0;padding:0}
html,body{width:1200px;height:2696px;overflow:hidden}
body{font-family:'Roboto',sans-serif;color:var(--ink);background:#fff;font-size:14px}
a{color:inherit;text-decoration:none}

/* top bar */
.topbar{height:40px;background:#fff;display:flex;justify-content:center;align-items:center;gap:18px;border-bottom:1px solid var(--line)}
.topbar-text{color:var(--orange);font-weight:700;font-size:13px;letter-spacing:.5px}
.topbar-btn{background:var(--red);color:#fff;font-size:12px;padding:6px 22px;border-radius:2px}

/* header */
.header{height:104px;display:flex;align-items:center;justify-content:space-between;padding:0 92px}
.brand{display:flex;align-items:center;gap:10px}
.brand-mark{width:18px;height:18px;border-radius:50%;background:var(--orange)}
.brand-name{font-size:30px;font-weight:700;color:var(--blue)}
.nav{display:flex;align-items:center;gap:30px;font-size:14px;color:#555}
.nav .active{color:var(--blue);border-bottom:2px solid var(--blue);padding-bottom:4px}
.nav-search{width:30px;height:30px;border:2px solid var(--orange);border-radius:50%;display:flex;align-items:center;justify-content:center}

/* hero */
.hero{position:relative;height:448px}
.hero-photo{position:absolute;inset:0;background:linear-gradient(100deg,#9aa0a6 0%,#c3c7cb 40%,#e3e4e5 70%,#d2d4d6 100%)}
.hero-content{position:absolute;left:150px;top:148px;color:#fff}
.hero-title{font-size:30px;font-weight:400;letter-spacing:1px;text-transform:uppercase}
.hero-sub{color:var(--yellow);font-size:17px;letter-spacing:2px;margin-top:6px;font-weight:500}
.pricing-box{margin-top:22px;width:220px;background:var(--green);padding:14px 18px 18px}
.pricing-title{font-size:22px;font-weight:500;color:#fff;display:flex;align-items:center;gap:8px}
.pricing-field{margin-top:12px;display:flex;height:26px}
.pricing-select{flex:1;background:#fff;color:#666;font-size:11px;display:flex;align-items:center;padding:0 8px}
.pricing-go{width:28px;background:var(--blue);color:#fff;font-size:11px;display:flex;align-items:center;justify-content:center}
.hero-dots{position:absolute;left:210px;bottom:14px;display:flex;gap:8px}
.hero-dots span{width:10px;height:10px;border-radius:50%;background:#fff;opacity:.6}
.hero-dots span:first-child{opacity:1;background:var(--blue)}

/* services */
.services{height:256px;display:flex;justify-content:center;gap:24px;padding-top:26px}
.service{width:168px;text-align:center}
.service-icon{width:78px;height:78px;border-radius:50%;background:var(--blue);margin:0 auto;display:flex;align-items:center;justify-content:center;border:4px solid #d6e4f2}
.service-title{color:var(--blue);font-weight:700;font-size:14px;margin-top:12px}
.service-text{font-size:10px;color:var(--muted);line-height:1.5;margin-top:6px}
.service-more{width:20px;height:20px;border-radius:50%;background:var(--blue);margin:10px auto 0;display:flex;align-items:center;justify-content:center}

/* stats */
.stats{position:relative;height:312px;color:#fff}
.stats-photo{position:absolute;inset:0;background:linear-gradient(180deg,#5b6066,#3d4247)}
.stats-inner{position:relative;text-align:center;padding-top:44px}
.stats-title{font-size:28px;font-weight:400}
.stats-row{display:flex;justify-content:center;gap:36px;margin-top:36px}
.stat{width:140px}
.stat svg{display:block;margin:0 auto 6px}
.stat-num{font-size:34px;font-weight:300}
.stat-label{font-size:10px;opacity:.8;line-height:1.4;margin-top:4px}

/* testimonials */
.testimonials{height:440px;padding-top:36px}
.section-title{text-align:center;color:var(--blue);font-size:30px;font-weight:400}
.clients{display:flex;justify-content:center;gap:60px;margin-top:38px;color:#444;font-weight:500;font-size:18px}
.testimonial{display:flex;justify-content:center;gap:36px;margin-top:40px}
.testimonial-photo{width:360px;height:250px;background:linear-gradient(120deg,#cfd6dc,#eef0f1 55%,#b9c3cb);border-top:6px solid var(--blue)}
.testimonial-body{width:420px;padding-top:20px}
.testimonial-head{font-size:20px;color:#444}
.testimonial-quote{font-size:12px;color:var(--muted);line-height:1.7;margin-top:14px;font-style:italic}
.testimonial-author{margin-top:16px;font-size:14px;color:#444}

/* blog */
.blog{height:500px;background:var(--soft);padding-top:34px}
.blog-cards{display:flex;justify-content:center;gap:26px;margin-top:36px}
.card{width:282px}
.card-photo{position:relative;height:200px}
.card-photo.a{background:linear-gradient(160deg,#9fb4c9,#d9e2ea)}
.card-photo.b{background:linear-gradient(180deg,#7fa2c8,#c9d5de)}
.card-photo.c{background:linear-gradient(140deg,#b5bfc5,#e6e8e6)}
.card-date{position:absolute;left:0;bottom:0;width:40px;height:48px;background:var(--green);color:#fff;text-align:center;font-size:16px;font-weight:700;padding-top:6px;line-height:1.1}
.card-date small{display:block;font-size:9px;font-weight:400}
.card-title{font-size:16px;font-weight:500;margin-top:14px}
.card-text{font-size:10px;color:var(--muted);line-height:1.6;margin-top:8px}
.card-meta{display:flex;gap:20px;font-size:10px;color:var(--muted);margin-top:12px}
.card-meta span::before{content:"";display:inline-block;width:8px;height:8px;border-radius:50%;background:var(--green);margin-right:5px}

/* contact */
.contact{height:260px;padding-top:32px}
.contact-title{text-align:center;font-size:26px;color:#444;font-weight:400}
.contact-form{width:420px;margin:28px auto 0;display:grid;grid-template-columns:1fr 1fr;gap:8px 16px}
.field{height:26px;border:1px solid var(--line);font-size:10px;color:#999;padding:7px 8px}
.contact-submit{grid-column:1/3;justify-self:center;background:var(--blue);color:#fff;font-size:12px;padding:7px 30px;margin-top:8px}

/* footer */
.footer{height:336px;background:var(--soft);border-top:1px solid var(--line)}
.footer-top{display:flex;justify-content:center;align-items:center;gap:70px;height:110px}
.footer-info{font-size:11px;color:#666;line-height:1.6}
.footer-info b{color:var(--blue);font-size:13px;font-weight:500}
.newsletter{background:#e7e7e7;height:80px;display:flex;align-items:center;justify-content:center;gap:16px}
.newsletter-label{font-size:14px;color:#555}
.newsletter-input{width:240px;height:28px;background:#fff;border:1px solid var(--line)}
.newsletter-btn{background:var(--red);color:#fff;font-size:11px;padding:7px 18px}
.footer-nav{display:flex;justify-content:center;gap:30px;font-size:12px;color:#666;padding-top:24px}
.footer-nav .active{color:var(--blue)}
.socials{display:flex;justify-content:center;gap:8px;margin-top:16px}
.socials span{width:22px;height:22px;border-radius:50%;background:var(--blue)}
.footer-bottom{display:flex;justify-content:space-between;font-size:9px;color:#999;padding:36px 92px 0}
</style>
</head>
<body>

<div class="topbar">
  <span class="topbar-text">GET YOUR FREE HR ASSESSMENT</span>
  <a class="topbar-btn" href="#">View Assessment</a>
</div>

<header class="header">
  <div class="brand"><span class="brand-mark"></span><span class="brand-name">VireloStaffHR</span></div>
  <nav class="nav">
    <a class="active" href="#">Home</a><a href="#">Services</a><a href="#">Broker</a><a href="#">Resources</a><a href="#">Contact</a><a href="#">Blog</a>
    <span class="nav-search"><svg width="14" height="14" viewBox="0 0 14 14"><circle cx="6" cy="6" r="4" fill="none" stroke="#f37122" stroke-width="2"/><line x1="9" y1="9" x2="13" y2="13" stroke="#f37122" stroke-width="2"/></svg></span>
  </nav>
</header>

<section class="hero">
  <div class="hero-photo" role="img" aria-label="Photo of a smiling businesswoman in the foreground with colleagues blurred in an office behind"></div>
  <div class="hero-content">
    <h1 class="hero-title">VireloStaffHR is outsourcing-based</h1>
    <p class="hero-sub">PAYROLL, SAFETY, COMPLIANCE</p>
    <div class="pricing-box">
      <div class="pricing-title"><svg width="18" height="18" viewBox="0 0 18 18"><path d="M3 9l4 4 8-9" fill="none" stroke="#fff" stroke-width="2.5"/></svg>Get FREE Pricing</div>
      <div class="pricing-field"><span class="pricing-select">HR Outsourcing</span><span class="pricing-go">GO</span></div>
    </div>
  </div>
  <div class="hero-dots"><span></span><span></span><span></span></div>
</section>

<section class="services">
  <div class="service">
    <div class="service-icon"><svg width="40" height="34" viewBox="0 0 40 34" fill="#fff"><circle cx="13" cy="9" r="6"/><circle cx="28" cy="9" r="6"/><path d="M2 32c0-9 5-13 11-13s11 4 11 13z"/><path d="M22 20c2-1 4-1 6-1 6 0 10 4 10 13H26"/></svg></div>
    <div class="service-title">HR Outsourcing</div>
    <p class="service-text">Hand off daily HR tasks to a team that knows state rules and keeps your files in order.</p>
    <div class="service-more"><svg width="8" height="8" viewBox="0 0 8 8"><path d="M2 1l4 3-4 3" fill="none" stroke="#fff" stroke-width="1.5"/></svg></div>
  </div>
  <div class="service">
    <div class="service-icon"><svg width="34" height="38" viewBox="0 0 34 38"><path d="M17 2l14 5v11c0 9-6 15-14 18C9 33 3 27 3 18V7z" fill="#fff"/><path d="M10 19l5 5 9-10" fill="none" stroke="#0255a3" stroke-width="3"/></svg></div>
    <div class="service-title">Safety</div>
    <p class="service-text">Workplace safety plans, training and checks that protect your people and your business.</p>
    <div class="service-more"><svg width="8" height="8" viewBox="0 0 8 8"><path d="M2 1l4 3-4 3" fill="none" stroke="#fff" stroke-width="1.5"/></svg></div>
  </div>
  <div class="service">
    <div class="service-icon"><svg width="38" height="38" viewBox="0 0 38 38"><circle cx="19" cy="19" r="16" fill="#fff"/><path d="M19 9v10l7 5" fill="none" stroke="#0255a3" stroke-width="3"/></svg></div>
    <div class="service-title">Payroll/Timekeeping</div>
    <p class="service-text">Accurate payroll runs and simple time tracking so every employee is paid right and on time.</p>
    <div class="service-more"><svg width="8" height="8" viewBox="0 0 8 8"><path d="M2 1l4 3-4 3" fill="none" stroke="#fff" stroke-width="1.5"/></svg></div>
  </div>
  <div class="service">
    <div class="service-icon"><svg width="30" height="38" viewBox="0 0 30 38"><rect x="2" y="2" width="26" height="34" rx="2" fill="#fff"/><path d="M8 12h14M8 18h14M8 24h9" stroke="#0255a3" stroke-width="2.5"/></svg></div>
    <div class="service-title">Benefits Administration</div>
    <p class="service-text">Plan setup, enrollment and ongoing benefits support handled for you year round.</p>
    <div class="service-more"><svg width="8" height="8" viewBox="0 0 8 8"><path d="M2 1l4 3-4 3" fill="none" stroke="#fff" stroke-width="1.5"/></svg></div>
  </div>
  <div class="service">
    <div class="service-icon"><svg width="40" height="32" viewBox="0 0 40 32" fill="#fff"><path d="M6 24c0-10 6-18 14-18s14 8 14 18z"/><rect x="2" y="24" width="36" height="5" rx="2"/><rect x="18" y="2" width="4" height="10"/></svg></div>
    <div class="service-title">Workers' Compensation</div>
    <p class="service-text">Coverage and claims help that keeps your team and your budget safe after an injury.</p>
    <div class="service-more"><svg width="8" height="8" viewBox="0 0 8 8"><path d="M2 1l4 3-4 3" fill="none" stroke="#fff" stroke-width="1.5"/></svg></div>
  </div>
</section>

<section class="stats">
  <div class="stats-photo" role="img" aria-label="Darkened photo of an HR team meeting around a table"></div>
  <div class="stats-inner">
    <h2 class="stats-title">We are the HR Professionals</h2>
    <div class="stats-row">
      <div class="stat"><svg width="26" height="26" viewBox="0 0 26 26" fill="#fff"><path d="M7 3h12v7a6 6 0 0 1-12 0z"/><rect x="11" y="16" width="4" height="5"/><rect x="7" y="21" width="12" height="3"/></svg><div class="stat-num">7/10</div><p class="stat-label">clients rate our HR support as the best they have used</p></div>
      <div class="stat"><svg width="26" height="26" viewBox="0 0 26 26" fill="#fff"><rect x="3" y="6" width="20" height="15" rx="2"/><rect x="9" y="3" width="8" height="4"/></svg><div class="stat-num">650</div><p class="stat-label">businesses served across the region</p></div>
      <div class="stat"><svg width="26" height="26" viewBox="0 0 26 26" fill="#fff"><circle cx="13" cy="8" r="5"/><path d="M3 24c0-7 4-10 10-10s10 3 10 10z"/></svg><div class="stat-num">94,000</div><p class="stat-label">employees paid through our payroll</p></div>
      <div class="stat"><svg width="26" height="26" viewBox="0 0 26 26" fill="#fff"><circle cx="9" cy="8" r="4"/><circle cx="18" cy="8" r="4"/><path d="M1 22c0-6 3-9 8-9s8 3 8 9zM15 13c5 0 10 3 10 9h-7"/></svg><div class="stat-num">13,500+</div><p class="stat-label">workers covered by our plans</p></div>
      <div class="stat"><svg width="26" height="26" viewBox="0 0 26 26" fill="#fff"><rect x="3" y="5" width="20" height="18" rx="2"/><rect x="3" y="5" width="20" height="5" fill="#ccc"/></svg><div class="stat-num">25</div><p class="stat-label">years of HR experience</p></div>
      <div class="stat"><svg width="26" height="26" viewBox="0 0 26 26" fill="#fff"><rect x="2" y="7" width="22" height="13" rx="2"/><circle cx="13" cy="13.5" r="3" fill="#555"/></svg><div class="stat-num">$31 Billion+</div><p class="stat-label">in payroll processed to date</p></div>
    </div>
  </div>
</section>

<section class="testimonials">
  <h2 class="section-title">Client Testimonials</h2>
  <div class="clients">
    <span>Arbelton</span><span>Lumeria</span><span>Norvik Group</span><span>Castavo</span><span>Meridale</span><span>Softrion</span>
  </div>
  <div class="testimonial">
    <div class="testimonial-photo" role="img" aria-label="Photo of two colleagues reviewing documents at a desk"></div>
    <div class="testimonial-body">
      <h3 class="testimonial-head">What our client says...</h3>
      <p class="testimonial-quote">“ Since moving our HR and payroll to this team, we spend far less time on paperwork and far more time growing. They answer fast, know every state rule we deal with, and have made our reviews, hiring and time keeping simple. We feel fully covered and truly supported every single week. ”</p>
      <p class="testimonial-author">– Dana Whitfield, Director of HR</p>
    </div>
  </div>
</section>

<section class="blog">
  <h2 class="section-title">Blog</h2>
  <div class="blog-cards">
    <article class="card">
      <div class="card-photo a" role="img" aria-label="Photo of glass office towers against a blue sky"><div class="card-date">01<small>MAR</small></div></div>
      <h3 class="card-title">Finibus Bonorum et Malorum</h3>
      <p class="card-text">Short notes on payroll rules, new state laws and smart ways to keep your team compliant all year.</p>
      <div class="card-meta"><span>Admin</span><span>12 Comments</span></div>
    </article>
    <article class="card">
      <div class="card-photo b" role="img" aria-label="Photo of a city skyline with tall towers"><div class="card-date">01<small>MAR</small></div></div>
      <h3 class="card-title">Finibus Bonorum et Malorum</h3>
      <p class="card-text">What business owners should know about hiring, onboarding and keeping good records from day one.</p>
      <div class="card-meta"><span>Admin</span><span>12 Comments</span></div>
    </article>
    <article class="card">
      <div class="card-photo c" role="img" aria-label="Photo of two business people shaking hands in an office"><div class="card-date">01<small>MAR</small></div></div>
      <h3 class="card-title">Finibus Bonorum et Malorum</h3>
      <p class="card-text">A simple guide to running fair employee reviews that help people grow and keep you covered.</p>
      <div class="card-meta"><span>Admin</span><span>12 Comments</span></div>
    </article>
  </div>
</section>

<section class="contact">
  <h2 class="contact-title">Talk to a Team Member Today</h2>
  <form class="contact-form">
    <div class="field">First Name</div><div class="field">Last Name</div>
    <div class="field">Company</div><div class="field">Phone</div>
    <div class="field">Email Address</div><div class="field">Message</div>
    <span class="contact-submit">Submit</span>
  </form>
</section>

<footer class="footer">
  <div class="footer-top">
    <div class="brand"><span class="brand-mark"></span><span class="brand-name">VireloStaffHR</span></div>
    <div class="footer-info"><b>Contact Info</b></div>
    <div class="footer-info">125 Example Avenue, Suite 200<br>Springfield, ST 00000<br>(555) 010-0142</div>
    <div class="footer-info">Get directions</div>
  </div>
  <div class="newsletter">
    <span class="newsletter-label">Subscribe Newsletter</span>
    <span class="newsletter-input"></span>
    <span class="newsletter-btn">Subscribe</span>
  </div>
  <nav class="footer-nav">
    <a class="active" href="#">Home</a><a href="#">Services</a><a href="#">Broker</a><a href="#">Resources</a><a href="#">Contact</a><a href="#">Blog</a>
  </nav>
  <div class="socials"><span></span><span></span><span></span><span></span></div>
  <div class="footer-bottom"><span>© 2024 VireloStaffHR. All rights reserved.</span><span>Privacy Policy | Terms of Use</span></div>
</footer>

</body>
</html>
```